Website for a company offering full serivce charging solutions for electric cars

The company "mero-kant" (english: "mero-edge") offering all-in-one-solutions for charging infrastructure for electric mobility.

There are four products:
1- Wallboxes for single-family homes
2- Solutions for property devloper/-management for property parking space
3- All-in-one-charging solution for municipalities/communities
4- Solutions for tourism/hotels/holiday appartments

The Website structure:
1. Main Page
2.1. Product Page Single Homes
2.2. Product Page Property Management / Parking
2.3. Product Page Municipality
2.4. Product Page Tourism
3. Contact Form / Request for information
4. Imprint / Legal

The Website should be built on Wordpress with a powerful possibility to simply add/modify specific landing pages.

We would like you to implement the website later and also maintain it if possible, but we would be able to do minor modifications by ourselfs (for A/B-Testing)

The website should be clear and simple, easy to understand.
Target group is mainly B2C without deeper knowledge of that topic.

It should suggest, that we will provide a very simple way to get the charging infrastructure done.

We need a contact form, maybe we will use Hubspot later.

Attached you will find a draft of the main page and a landing page (for 2.2) - it is just the content, please ignore the design. We would love to let you create a suitable design.
Also you will find some drafts a bit different for the same story.

I added also a few stock photos, but they don't need to be used! If you have better ideas, you are welcome!

Industry/Entity Type

Charging/Electric mobility

Number of Pages Required

2 page

Font styles to use
Sans Serif

Requirements
Must have
• Based on Wordpress, and the designer should be able to implement it on Wordpress on a later step

```html
<!DOCTYPE html>
<html lang="de">
<head>
<meta charset="utf-8">
<title>mero-kant – einfach mehr als laden</title>
<link rel="stylesheet" href="https://fonts.googleapis.com/css2?family=Exo+2:wght@400;500;600;700&family=Open+Sans:wght@400;600;700&display=swap">
<style>
:root{
  --navy:#131a2d;
  --navy-2:#171f36;
  --navy-3:#0f1526;
  --pink:#e5178c;
  --purple:#7b3fd3;
  --violet:#9a4fe0;
  --white:#ffffff;
  --muted:#c9cde0;
  --grey:#8a90a8;
}
*{box-sizing:border-box;margin:0;padding:0}
html,body{width:1200px;height:4329px;overflow:hidden}
body{background:var(--navy);color:var(--white);font-family:"Open Sans",Arial,sans-serif;position:relative}
.display{font-family:"Exo 2",Arial,sans-serif}
section,header,footer{position:absolute;left:0;width:1200px}

/* header */
.site-header{top:0;height:76px;z-index:5;background:rgba(15,21,38,.55)}
.brand{position:absolute;left:104px;top:16px;display:flex;align-items:center;gap:10px}
.brand-dot{width:36px;height:36px;border-radius:50%;border:3px solid var(--pink)}
.brand-name{font-family:"Exo 2",sans-serif;font-weight:600;font-size:24px;line-height:24px;color:var(--white)}
.brand-tag{font-size:12px;color:var(--muted);margin-top:2px}
.main-nav{position:absolute;left:455px;top:0;height:76px;display:flex;gap:0;font-size:14px}
.main-nav a{color:var(--white);text-decoration:none;height:76px;line-height:74px;padding:0 0;margin-right:58px;position:relative}
.main-nav a.active::after{content:"";position:absolute;left:0;right:0;bottom:0;height:2px;background:var(--pink)}
.btn-contact{position:absolute;left:970px;top:19px;width:120px;height:38px;background:linear-gradient(90deg,var(--purple),var(--pink));font-size:13px;font-weight:600;text-align:center;line-height:38px;color:var(--white);box-shadow:0 0 10px rgba(229,23,140,.6)}

/* hero */
.hero{top:0;height:698px}
.hero-photo{position:absolute;inset:0;background:radial-gradient(circle at 78% 30%,#6fb6ff 0%,#2550c8 18%,#1a2b6a 38%,#121a36 70%),var(--navy)}
.hero-shade{position:absolute;inset:0;background:linear-gradient(90deg,rgba(15,21,38,.85) 0%,rgba(15,21,38,.4) 55%,rgba(15,21,38,0) 100%)}
.hero-title{position:absolute;left:122px;top:222px;font-size:58px;line-height:54px;font-weight:400}
.hero-title b{font-weight:700}
.hero-lead{position:absolute;left:122px;top:355px;width:520px;font-size:21px;line-height:30px}
.btn-primary{position:absolute;display:block;background:linear-gradient(90deg,var(--purple),var(--pink));color:var(--white);font-family:"Exo 2",sans-serif;font-weight:700;text-align:center;text-decoration:none}
.hero .btn-primary{left:122px;top:445px;width:156px;height:43px;line-height:43px;font-size:14px}

.connector{position:absolute;left:599px;width:2px;background:var(--grey)}
.connector::after{content:"";position:absolute;left:-4px;bottom:-4px;width:10px;height:10px;border-radius:50%;background:var(--pink)}

/* hexagon media */
.hex{position:absolute}
.hex svg.frame{position:absolute;inset:0;overflow:visible}
.hex-fill{position:absolute;clip-path:polygon(50% 0,100% 25%,100% 75%,50% 100%,0 75%,0 25%)}

/* about */
.about{top:740px;height:588px;background:linear-gradient(180deg,var(--navy) 0%,var(--navy-2) 75%,#1b2440 100%)}
.section-title{font-family:"Exo 2",sans-serif;font-weight:700;font-size:36px;line-height:40px}
.about .section-title{position:absolute;left:597px;top:96px}
.section-title .pink{color:var(--pink)}
.section-title .violet{color:var(--violet);font-weight:400}
.about .lead{position:absolute;left:597px;top:162px;width:510px;font-size:17px;line-height:26px}
.about .body{position:absolute;left:597px;top:280px;width:510px;font-size:14px;line-height:26px}

/* privat */
.privat{top:1328px;height:709px;background:var(--navy-2)}
.ask-title{position:absolute;top:56px;left:0;width:1200px;text-align:center;font-family:"Exo 2",sans-serif;font-size:27px;line-height:34px;font-weight:600}
.ask-title span{font-weight:400}
.privat .section-title{position:absolute;left:134px;top:202px;color:var(--pink);font-size:38px}
.underline{position:absolute;height:3px;width:52px;background:var(--white)}
.plain-list{position:absolute;list-style:none;font-size:13px;line-height:16px}
.plain-list li{margin-bottom:8px}
.privat .plain-list{left:134px;top:273px;width:500px}

/* business */
.business{top:2037px;height:560px;background:linear-gradient(90deg,#6a2fc6 0%,#8a34c0 40%,#d01a95 75%,#e2137f 100%)}
.business-photo{position:absolute;left:330px;top:120px;width:720px;height:380px;background:radial-gradient(ellipse at 50% 60%,rgba(255,255,255,.22),rgba(255,255,255,0) 65%)}
.business .section-title{position:absolute;left:0;width:1200px;text-align:center;top:62px;font-size:38px;font-weight:600}
.arrow-list{position:absolute;list-style:none;font-size:13px;font-weight:600;line-height:17px}
.arrow-list li{padding-left:15px;position:relative;margin-bottom:8px}
.arrow-list li::before{content:"";position:absolute;left:0;top:4px;width:6px;height:6px;border-right:2px solid currentColor;border-bottom:2px solid currentColor;transform:rotate(-45deg)}
.arrow-list .sub{font-weight:400;margin:4px 0 12px;padding:0}
.arrow-list .sub li{margin-bottom:2px}
.business .col-left{left:123px;top:168px;width:480px}
.business .col-right{left:649px;top:173px;width:500px}
.business .col-right li{margin-bottom:17px}

/* kommune */
.kommune{top:2597px;height:672px;background:var(--navy-3)}
.kommune .section-title{position:absolute;left:647px;top:88px;font-size:38px;font-weight:600}
.kommune .arrow-list{left:647px;top:158px;width:510px;font-weight:400;font-size:13px;line-height:16px}
.kommune .arrow-list li{margin-bottom:12px}
.kommune .arrow-list li::before{color:var(--pink)}

/* contact */
.contact{top:3269px;height:714px;background:linear-gradient(180deg,#151c33 0%,#131a2d 100%)}
.contact-scene{position:absolute;left:80px;top:380px;width:980px;height:260px;background:radial-gradient(ellipse at 50% 55%,#5f9ee8 0%,#2a3f86 18%,rgba(35,45,90,.6) 45%,rgba(19,26,45,0) 75%)}
.contact .section-title{position:absolute;left:0;width:1200px;text-align:center;top:58px;font-size:38px;font-weight:600}
.contact .section-title span{font-weight:400}
.field{position:absolute;background:var(--white);color:#555;font-size:13px;display:flex;align-items:center;gap:10px;padding-left:18px}
.field svg{width:16px;height:16px}
.f-name{left:190px;top:134px;width:407px;height:50px}
.f-mail{left:190px;top:195px;width:407px;height:54px}
.f-phone{left:190px;top:257px;width:407px;height:54px}
.f-msg{left:603px;top:134px;width:405px;height:177px;align-items:flex-start;padding-top:20px}
.contact .btn-primary{left:497px;top:341px;width:194px;height:54px;line-height:54px;font-size:17px;box-shadow:0 0 12px rgba(229,23,140,.5)}

/* footer */
.site-footer{top:3983px;height:279px;background:var(--navy)}
.foot-brand{position:absolute;left:110px;top:60px;display:flex;flex-direction:column;align-items:center;gap:14px}
.foot-brand .brand-dot{width:60px;height:60px;border-width:5px}
.foot-brand .brand-name{font-size:36px;line-height:36px}
.foot-col{position:absolute;top:60px;border-left:3px solid var(--pink);padding-left:22px}
.foot-col h4{font-family:"Exo 2",sans-serif;font-size:17px;font-weight:600;margin-bottom:14px}
.foot-col a{display:block;color:var(--grey);text-decoration:none;font-size:14px;line-height:31px}
.c1{left:395px}.c2{left:652px}.c3{left:866px}
.socials{display:flex;gap:8px;margin-top:2px}
.socials span{width:33px;height:33px;border-radius:50%;background:linear-gradient(135deg,var(--purple),var(--pink))}
.bottom-bar{position:absolute;left:0;top:4262px;width:1200px;height:67px;background:var(--navy-3);text-align:center;line-height:67px;font-size:13px;color:var(--muted)}
</style>
</head>
<body>

<header class="site-header">
  <div class="brand">
    <span class="brand-dot"></span>
    <div><div class="brand-name">mero-kant.de</div><div class="brand-tag">einfach mehr als laden</div></div>
  </div>
  <nav class="main-nav">
    <a class="active" href="#">LÖSUNGEN</a>
    <a href="#">UNTERNEHMEN</a>
    <a href="#">SERVICES</a>
    <a href="#">KARRIERE</a>
  </nav>
  <a class="btn-contact" href="#">KONTAKT</a>
</header>

<section class="hero">
  <div class="hero-photo" role="img" aria-label="Ladestecker in einer blau leuchtenden Ladebuchse eines Elektroautos"></div>
  <div class="hero-shade"></div>
  <h1 class="hero-title display"><b>mero-kant ist</b><br>Ihr Partner</h1>
  <p class="hero-lead">wenn das Laden nicht nur einfach, sondern die Umsetzung auch aus einer Hand kommen soll</p>
  <a class="btn-primary" href="#">LEARN MORE</a>
</section>

<div class="connector" style="top:698px;height:42px"></div>

<section class="about">
  <div class="hex" style="left:134px;top:58px;width:396px;height:420px">
    <svg class="frame" viewBox="0 0 396 420">
      <polygon points="198,2 394,107 394,313 198,418 2,313 2,107" fill="none" stroke="#7b3fd3" stroke-width="2" opacity=".7"/>
      <circle cx="118" cy="30" r="5" fill="#e5178c"/>
      <circle cx="56" cy="348" r="5" fill="#e5178c"/>
      <circle cx="376" cy="330" r="5" fill="#7b3fd3"/>
    </svg>
    <div class="hex-fill" style="left:22px;top:24px;width:352px;height:372px;background:radial-gradient(circle at 60% 40%,#ffffff 0%,#a9c7ff 25%,#2f5de0 50%,#e8ecf5 75%)" role="img" aria-label="Weißer Ladestecker mit blauem Leuchtring"></div>
  </div>
  <h2 class="section-title"><span class="pink">ORVEL</span> <span class="violet">MERO KANT</span></h2>
  <p class="lead">Wir bieten Lösungen sowohl für Privatkunden, Geschäftskunden als auch Kommunen an, die schnell, fair und ohne Eigenleistung zu einer smarten Ladelösung für E-Fahrzeuge kommen möchten.</p>
  <p class="body">Von der Beratung, über die Installation, Inbetriebnahme bis zur Abrechnung und Wartung bekommen Sie bei mero-kant alles aus einer Hand. Auf Wunsch vermieten wir auch die Ladetechnik und übernehmen im gewerblichen Bereich die direkte Abrechnung mit dem Nutzer. Für Kommunen bieten wir den kostenfreien Full-Service an und beteiligen die Gemeinden an der Nutzung der Infrastruktur.</p>
</section>

<div class="connector" style="top:1286px;height:67px"></div>

<section class="privat">
  <h2 class="ask-title">FRAGEN SIE UNS NACH DER AUF IHRE INDIVIDUELLEN<br><span>BEDÜRFNISSE ZUGESCHNITTENEN LÖSUNG:</span></h2>
  <h2 class="section-title">ALS PRIVATKUNDE</h2>
  <div class="underline" style="left:134px;top:250px"></div>
  <ul class="plain-list">
    <li>Bestandsanalyse mit umfangreicher Beratung über die Möglichkeiten der Umsetzung</li>
    <li>Prüfung und Übernahme der Anmeldung verfügbarer Fördermöglichkeiten</li>
    <li>Auswahl an smarten Wallbox Lösungen, passend für Ihr Fahrzeug und Ihre Bedürfnisse</li>
    <li>Installation inkl. aller notwendigen Materialien und Tätigkeiten (Durchbrüche, Erdarbeiten, etc.)</li>
    <li>Inbetriebnahme und Einweisung in die Ladetechnik</li>
    <li>Jährlich technische Wartung nach DGUV3</li>
    <li>Reparaturservice, unter Berücksichtigung der geltenden Garantie Ansprüche</li>
    <li>Installation inkl. aller notwendigen Materialien und Tätigkeiten (Durchbrüche, Erdarbeiten, etc.)</li>
    <li>Inbetriebnahme und Einweisung in die Ladetechnik</li>
    <li>Jährlich technische Wartung nach DGUV3</li>
    <li>Reparaturservice, unter Berücksichtigung der geltenden Garantie Ansprüche</li>
  </ul>
  <div class="hex" style="left:669px;top:159px;width:444px;height:488px">
    <svg class="frame" viewBox="0 0 444 488">
      <polygon points="222,2 442,124 442,364 222,486 2,364 2,124" fill="none" stroke="#9a4fe0" stroke-width="2" opacity=".8"/>
    </svg>
    <div class="hex-fill" style="left:24px;top:26px;width:396px;height:436px;background:linear-gradient(135deg,#c9ccd4 0%,#5b6a8a 40%,#2b57b8 60%,#20263a 100%)" role="img" aria-label="Ladesäule mit blauem Ladestecker"></div>
  </div>
</section>

<section class="business">
  <div class="business-photo" role="img" aria-label="Elektroauto an einer Ladestation, transparent im Hintergrund"></div>
  <h2 class="section-title">ALS GESCHÄFTSKUNDE</h2>
  <div class="underline" style="left:574px;top:110px"></div>
  <ul class="arrow-list col-left">
    <li>Durchführung einer individuellen Bedarfsanalyse inkl. Ermittlung der</li>
    <li>Anforderungen für:
      <ul class="sub arrow-list" style="position:static">
        <li>Haus- und Immobilienverwaltungen</li>
        <li>Dienstleistungs- und Handelsunternehmen</li>
        <li>Hotel und Beherbergungsbetriebe</li>
        <li>Parkraum- und Parkhausbetreiber</li>
        <li>Tourismus, Sport- und Freizeiteinrichtungen</li>
      </ul>
    </li>
    <li>Planung und Projektierung des Installationsaufwands inkl.</li>
    <li>Materialverbrauch</li>
    <li style="margin-top:16px">Leasing oder Kauf der Hardware</li>
    <li style="margin-top:16px">Normgerechte Installation der Ladeinfrastruktur inkl. Durchbruch-,</li>
    <li>Brandschutz- und Erdarbeiten</li>
  </ul>
  <ul class="arrow-list col-right">
    <li>Bei Bestandsbauten Integration der Ladeinfrastruktur in die</li>
    <li>Gebäudesystemtechnik und ggf. Anpassung des Netzanschlusses</li>
    <li>Inbetriebnahme der Anlage inkl. Prüf- und Messprotokollen</li>
    <li>Wiederkehrende technische Prüfung der Anlage nach DGUV 3</li>
    <li>Austausch und Reparatur Service</li>
    <li style="line-height:26px">Unterstützung bei der mtl. Nutzungsabrechnung und Einbindung in Ihre vorhandene Abrechnungssysteme</li>
    <li>ODER direkte Abrechnung mit den Nutzern</li>
  </ul>
</section>

<section class="kommune">
  <div class="hex" style="left:114px;top:92px;width:444px;height:488px">
    <svg class="frame" viewBox="0 0 444 488">
      <polygon points="222,2 442,124 442,364 222,486 2,364 2,124" fill="none" stroke="#9a4fe0" stroke-width="2" opacity=".8"/>
    </svg>
    <div class="hex-fill" style="left:24px;top:26px;width:396px;height:436px;background:radial-gradient(circle at 40% 50%,#49d07a 0%,#2a6a45 22%,#9aa4b4 48%,#4a6aa0 80%)" role="img" aria-label="Ladestecker mit grünem Leuchtring an einem silbernen Elektroauto"></div>
  </div>
  <h2 class="section-title">ALS KOMMUNE</h2>
  <ul class="arrow-list">
    <li>Konzeptionierung möglicher Ladeinfrastrukturen innerhalb Ihrer Gemeinde</li>
    <li>Planung und Projektsteuerung inkl. sämtlicher behördlicher Genehmigungsverfahren und Beantragung von Fördermitteln</li>
    <li>Fachgerechte Installation und Inbetriebnahme</li>
    <li>Regelmäßige Wartung gemäß Vorschrif</li>
    <li>Reparatur und Kundenservice</li>
    <li>Direkte Abrechnung mit dem Nutzer</li>
    <li>Beteiligung der Gemeinde am Umsatz</li>
    <li>Möglichkeit der Integration von Bonusprogrammen, mit denen der lokale Einzelhandel beworben wird</li>
    <li>von Fördermitteln<br>Fachgerechte Installation und Inbetriebnahme</li>
    <li>Regelmäßige Wartung gemäß Vorschrif</li>
    <li>Reparatur und Kundenservice</li>
    <li>Direkte Abrechnung mit dem Nutzer</li>
    <li>Beteiligung der Gemeinde am Umsatz</li>
    <li>Möglichkeit der Integration von Bonusprogrammen, mit denen der lokale Einzelhandel beworben wird</li>
  </ul>
</section>

<section class="contact">
  <div class="contact-scene" role="img" aria-label="Elektroauto an einer Ladesäule mit leuchtendem Batteriesymbol"></div>
  <h2 class="section-title">CONTACT <span>US</span></h2>
  <div class="underline" style="left:494px;top:102px;width:100px"></div>
  <div class="field f-name"><svg viewBox="0 0 16 16" fill="none" stroke="#777" stroke-width="1.3"><circle cx="8" cy="5" r="3"/><path d="M2 15c0-3.5 2.7-5.5 6-5.5s6 2 6 5.5"/></svg>Your Name*</div>
  <div class="field f-mail"><svg viewBox="0 0 16 16" fill="none" stroke="#777" stroke-width="1.3"><rect x="1" y="3" width="14" height="10"/><path d="M1 3l7 6 7-6"/></svg>Email address*</div>
  <div class="field f-phone"><svg viewBox="0 0 16 16" fill="#777"><path d="M3 1l3 3-1.5 2c1 2 2.5 3.5 4.5 4.5L11 9l3 3-2 2C6.5 13.5 2.5 9.5 1 3z"/></svg>Phone number*</div>
  <div class="field f-msg">Leave Message</div>
  <a class="btn-primary" href="#">SUBMIT NOW</a>
</section>

<footer class="site-footer">
  <div class="foot-brand">
    <span class="brand-dot"></span>
    <span class="brand-name">mero-kant.de</span>
  </div>
  <div class="foot-col c1"><h4>NAVIGATION</h4><a href="#">AGB</a><a href="#">Datenschutzerklärung</a><a href="#">Impressum</a></div>
  <div class="foot-col c2"><h4>RESOURCES</h4><a href="#">Kontakt</a><a href="#">Karriere</a><a href="#">FAQs</a></div>
  <div class="foot-col c3"><h4>FOLLOW US</h4><div class="socials"><span></span><span></span><span></span><span></span></div></div>
</footer>
<div class="bottom-bar">© 2022 mero-kant GmbH</div>

</body>
</html>
```